Label Design for American Pet Health Startup

We need your help in creating a line-up of labels for our upcoming products. The products will come in two different sizes/shapes. We have a logo (sourced form GraphiHive!) to start from and a pretty extensive brief (see attached.) The winning design will be bold, simple, and create a strongly branded look to the whole line while allowing consumers to easily sort through the different SKUs.

The logo and other existing design elements are in the attached powerpoint. I will also post some of the source files.

If you choose to compete for this project, please read the creative brief and the powerpoint very carefully before starting.

Thank you for your time and consideration.

Target Market(s)

Pet owners (dog owners, initially) who care deeply about their pets. Their pets are older and may not be thriving the way they once were. The owners want their pets to have the highest quality of life possible, for as long as is practical. They take their pets frequently to the vet and have great faith in veterinary medicine, but they also believe that dietary supplements may have a beneficial effect. They believe this to be possible because they take supplements themselves.

They are probably older--empty nesters or soon to be. They’ve owned their dog for five years or more, or have rescued an older dog from a shelter. Their dog is, in many ways, a full member of their family.

Industry/Entity Type

Pet Care

Font styles to use
Sans Serif

Requirements
Must have
• Please see the attached brief for this detail. I have cut and paste it into this form but it doesn't translate well. Reading the Word document will be easier and the links will work.
• Packaging Creative Considerations: The product packaging needs to . . .
• • Have a strong, branded line look.
• - The logo has already been developed, and I would like you to be guided in your design choices by its structure and color, but I am open to deviations from the existing work if it leads to a strong design
• • Use color or some other design elements to distinguish each SKU from the other
• • Be bold and simple. This product will typically be merchandised online, with very small images of the packaging. Simple and bold design elements will ensure that the products are both noticed and understood.
• - The product will likely be contained within white plastic or aluminum (silver) bottles with white caps/pumps. However, if you believe your design concepts would benefit from a particular color of bottle/container, please illustrate that, as that would be possible to execute.
• • Communicate that these products are for pets without using any clichés. This category is full of packaging with stock photos of dogs and cats. Please avoid this at all costs. Instead, please unleash your creativity to illustrate the products’ nature/purposes.
• A couple of packaging designs I would like you to draw inspiration from:
• o Vemo. This line is for human supplements/vitamins. Notice the strong line look, the simple and bold graphics, and the smart use of color and other design elements to differentiate the SKUs (while still holding it together as a single brand.)
• o Tundo. This line is for pets. Again, notice the strong line look, the smart use of color to differentiate the SKUs, and the simple and bold presentation that translates so well on the screen.
• o Corvalune. This design is not as good as the first two, but it does accomplish several of the brief’s objectives and the packaging is likely to be very similar to what your design will eventually be affixed to.
• Design Deliverables: A great submission will illustrate its strength by showing how the design translates across all the expected SKUs. To accomplish, this, I would recommend using the “functional maps” I’ve included in the attached Powerpoint document to:
• o First illustrate, in greater size and detail, one SKU each of the two families (one oil SKU and one supplement SKU)
• o Then illustrate how each of those designs extends across the rest of the family. That illustration can be less detailed. We just need to see how the colors and other design elements extend.
Should not have
• No stock images of cats or dogs; please avoid junking up the designs with too many elements

```html
<!DOCTYPE html>
<html lang="en">
<head>
<meta charset="utf-8">
<title>Tailwell Oil Labels</title>
<link href="https://fonts.googleapis.com/css2?family=Montserrat:wght@400;500;600&family=Didact+Gothic&display=swap" rel="stylesheet">
<style>
  :root {
    --page: #f4f4f4;
    --label: #ffffff;
    --ink: #111111;
    --grey: #6e6e6e;
    --muted: #8a8a8a;
    --teal: #1aa6b7;
    --salmon: #f26c55;
    --gold: #cda62c;
    --edge: #e2e2e2;
  }
  * { box-sizing: border-box; margin: 0; padding: 0; }
  html, body { width: 1200px; height: 1040px; overflow: hidden; }
  body {
    background: var(--page);
    position: relative;
    font-family: "Montserrat", sans-serif;
  }
  .label {
    position: absolute;
    top: 248px;
    width: 340px;
    height: 712px;
    background: var(--label);
    border: 1px solid var(--edge);
    border-radius: 60px 60px 24px 24px;
    text-align: center;
  }
  .label--salmon { left: 136px; --accent: var(--salmon); }
  .label--omega { left: 716px; --accent: var(--gold); }
  .label > * { position: absolute; left: 0; right: 0; }
  .brand {
    top: 132px;
    font-weight: 400;
    font-size: 42px;
    color: var(--grey);
    letter-spacing: 0.5px;
    display: flex;
    justify-content: center;
    align-items: center;
    gap: 10px;
  }
  .brand-dot {
    width: 14px; height: 14px;
    border-radius: 50%;
    background: var(--teal);
  }
  .title {
    top: 214px;
    font-weight: 600;
    font-size: 43px;
    line-height: 52px;
    letter-spacing: 0.5px;
  }
  .title .line { display: block; }
  .title .ink { color: var(--ink); }
  .title .accent { color: var(--accent); }
  .benefit {
    top: 318px;
    font-size: 17.5px;
    font-weight: 500;
    color: var(--grey);
    letter-spacing: 0.3px;
  }
  .emblem {
    top: 352px;
    left: 120px;
    right: auto;
    width: 100px;
    height: 148px;
    background: var(--accent);
  }
  .supplement {
    top: 508px;
    font-family: "Didact Gothic", sans-serif;
    font-size: 25px;
    color: var(--ink);
  }
  .audience {
    top: 537px;
    font-size: 22px;
    font-weight: 600;
    color: var(--accent);
    letter-spacing: 0.8px;
  }
  .origin {
    top: 586px;
    left: 81px;
    right: auto;
    width: 178px;
    height: 68px;
    border: 1px solid var(--teal);
    font-family: "Didact Gothic", sans-serif;
    font-size: 16px;
    line-height: 19px;
    color: var(--teal);
    display: flex;
    flex-direction: column;
    justify-content: center;
  }
  .volume {
    top: 668px;
    font-size: 12px;
    color: var(--muted);
    letter-spacing: 0.3px;
  }
  .label--omega .volume { font-weight: 600; }
</style>
</head>
<body>

  <section class="label label--salmon">
    <div class="brand"><span class="brand-dot"></span>Tailwell</div>
    <h1 class="title"><span class="line ink">PURE</span><span class="line accent">SALMON OIL</span></h1>
    <p class="benefit">Supports Healthy Coat &amp; Skin</p>
    <div class="emblem" role="img" aria-label="Salmon-coloured oil drop emblem with dog and cat profiles"></div>
    <p class="supplement">All Natural Supplement</p>
    <p class="audience">FOR DOGS + CATS</p>
    <div class="origin"><span>Made in USA</span><span>with 100%</span><span>Wild Alaskan Salmon</span></div>
    <p class="volume">Net 32 FL OZ / 946 ML</p>
  </section>

  <section class="label label--omega">
    <div class="brand"><span class="brand-dot"></span>Tailwell</div>
    <h1 class="title"><span class="line accent">OMEGA 3</span><span class="line ink">FISH OIL</span></h1>
    <p class="benefit">Supports Healthy Coat &amp; Skin</p>
    <div class="emblem" role="img" aria-label="Gold oil drop emblem with dog and cat profiles"></div>
    <p class="supplement">All Natural Supplement</p>
    <p class="audience">FOR DOGS + CATS</p>
    <div class="origin"><span>Made in USA</span><span>with Atlantic Sardines</span><span>&amp; Anchovies</span></div>
    <p class="volume">Net 32 FL OZ / 946 ML</p>
  </section>

</body>
</html>
```